Ridgeway Builders, Inc. Concrete cutting special flyer , 10% off for new customers

Flyer to send to potential customers and business associates and general contractors - specializing in Concrete-Flatwork
Concrete Repair
Concrete Sidewalks
Patios & Driveways
Stoops, Porches And Staircase
Foundation Contractors--Concrete
Facade Restoration
Concrete
Patios
Driveways
Walkways
Commercial Concrete Work
Concrete Restoration
Building Alterations
Foundations - Concrete
Concrete Repairs
rbwxpo.com

Target Market(s)

Homeowners, business owners & general contractors

Industry/Entity Type

Construction

Font styles to use
Serif

Colors
FFC000
F8CF3A
FAE287
FDF2CF
FEFAEE
EB3D1F
EC4F4E
F09395
F8D3D4
FCEDEE

Requirements
Must have
• General Contracting, masonry - Must have Logo Please see list of services Ridgeway Builders NY, Inc., has to offer. Concrete-Flatwork Concrete Repair Concrete Sidewalks Patios & Driveways Stoops, Porches And Staircase Foundation Contractors--Concrete Facade Restoration Concrete Patios Driveways Walkways Commercial Concrete Work Concrete Restoration Building Alterations Foundations - Concrete Concrete Repairs
Nice to have
• List of services - Logo - Black & Gold with a bold color to stand out (preferably reds)

```html
<!DOCTYPE html>
<html lang="en">
<head>
<meta charset="utf-8">
<title>Ridgeway Builders NY, Inc. – Services Flyer</title>
<link href="https://fonts.googleapis.com/css2?family=Open+Sans:wght@400;600;700;800&display=swap" rel="stylesheet">
<style>
  :root {
    --green: #1e3a27;
    --green-deep: #173021;
    --gold: #c9a43a;
    --gold-light: #d8b855;
    --ink: #2c2c2c;
    --paper: #f7f7f5;
    --backdrop: #6e6e6e;
  }
  * { box-sizing: border-box; margin: 0; padding: 0; }
  html, body { width: 1200px; height: 1074px; overflow: hidden; }
  body {
    background: var(--backdrop);
    font-family: "Open Sans", Arial, sans-serif;
    position: relative;
  }
  .flyer {
    position: absolute; left: 240px; top: 32px;
    width: 720px; height: 1010px;
    background: var(--paper);
    overflow: hidden;
    box-shadow: 0 10px 30px rgba(0,0,0,.35);
  }
  .brand {
    position: absolute; left: 58px; top: 46px;
    display: flex; align-items: center; gap: 10px;
    color: var(--green); font-weight: 800; font-size: 19px; line-height: 1.1;
  }
  .brand-mark { width: 26px; height: 26px; background: var(--green); flex: none; }
  .contact {
    position: absolute; right: 60px; top: 92px; text-align: right;
    color: var(--green); font-weight: 700; font-size: 20px; line-height: 1.3;
  }
  .contact .num { color: var(--gold); }
  .hero-photo {
    position: absolute; left: 60px; top: 152px; width: 640px; height: 408px;
    background: linear-gradient(110deg, #8a6552 0%, #b48a6e 38%, #c9b7a6 62%, #9b3b33 78%, #a98a5e 100%);
  }
  .hero-banner {
    position: absolute; left: 40px; top: 205px; width: 360px; height: 132px;
    background: var(--green); padding: 16px 22px 0 26px;
  }
  .hero-banner h1 {
    color: var(--gold-light); font-size: 25px; font-weight: 700; line-height: 1.05; text-transform: uppercase;
  }
  .hero-banner p {
    color: #e9e9e4; font-size: 12px; line-height: 1.35; margin-top: 6px;
  }
  .offer {
    position: absolute; right: 30px; top: 200px; width: 136px; height: 136px;
  }
  .offer-text {
    position: absolute; inset: 0; display: flex; flex-direction: column;
    align-items: center; justify-content: center; color: #fff; line-height: 1.05;
  }
  .offer-text .small { font-size: 14px; }
  .offer-text .big { color: var(--gold-light); font-size: 36px; font-weight: 800; margin: 2px 0; }
  .services-tab {
    position: absolute; left: 380px; top: 520px; width: 300px; height: 64px;
    background: var(--green); color: var(--gold-light);
    font-size: 32px; font-weight: 700; display: flex; align-items: center; justify-content: center;
  }
  .site-photo {
    position: absolute; left: 58px; top: 412px; width: 312px; height: 182px;
    background: linear-gradient(160deg, #7b8e6a 0%, #5c5a48 45%, #6e5e44 70%, #b8963e 100%);
  }
  .info { position: absolute; left: 58px; width: 312px; color: var(--ink); }
  .info h2 { font-size: 26px; font-weight: 800; color: var(--green-deep); line-height: 1.1; }
  .info h2 .accent { color: var(--gold); }
  .info p { font-size: 12.5px; line-height: 1.35; margin-top: 6px; }
  .what { top: 612px; }
  .why { top: 772px; }
  .services {
    position: absolute; left: 396px; top: 604px; list-style: none;
    color: #3a3a3a; font-weight: 600; font-size: 15.5px; line-height: 17.2px;
  }
  .services li { display: flex; align-items: center; gap: 9px; }
  .services svg { width: 12px; height: 12px; flex: none; }
  .footer-rule { position: absolute; left: 0; right: 0; top: 886px; height: 3px; background: var(--gold); }
  .footer {
    position: absolute; left: 0; right: 0; top: 896px; bottom: 0; background: var(--green);
  }
  .footer .line { position: absolute; left: 30px; right: 30px; height: 1px; background: var(--gold); opacity: .7; }
  .footer .web {
    position: absolute; left: 0; right: 0; top: 22px; text-align: center;
  }
  .footer .web span {
    background: var(--paper); color: var(--gold); padding: 0 14px;
    font-size: 20px; letter-spacing: 7px; font-weight: 600;
  }
  .footer .web-line { position: absolute; left: 60px; right: 60px; top: 36px; height: 1px; background: var(--paper); }
</style>
</head>
<body>
  <main class="flyer">
    <div class="brand"><span class="brand-mark"></span><span>Ridgeway Builders<br>NY, Inc.</span></div>

    <div class="contact">Call or Text <span class="num">555-014-2283</span><br>or <span class="num">555-019-4470</span></div>

    <div class="hero-photo" role="img" aria-label="Builder in a plaid shirt holding a yellow hard hat, wearing a leather tool belt, in front of a brick wall"></div>

    <div class="hero-banner">
      <h1>Excavation Concrete<br>Structural</h1>
      <p>We'll Get The Job Done Rite The first Time!! NY'S Leading Excavation, Foundation, Waterproofing and Flat Roof Specialists</p>
    </div>

    <div class="offer">
      <svg viewBox="0 0 136 136" width="136" height="136" aria-hidden="true">
        <circle cx="68" cy="68" r="66" fill="var(--green)"/>
        <circle cx="68" cy="68" r="54" fill="none" stroke="var(--gold)" stroke-width="2"/>
      </svg>
      <div class="offer-text"><span class="small">New</span><span class="small">Customers</span><span class="big">10%</span><span class="small">off</span></div>
    </div>

    <div class="site-photo" role="img" aria-label="Excavator and compact track loader on a cleared dirt job site"></div>

    <div class="services-tab">OUR SERVICES</div>

    <section class="info what">
      <h2>WHAT WE DO ?</h2>
      <p>Our projects include both Residential and Commercial construction and repairs/restorations. Occupied and fully operational job sites are never a problem. And we can also plan, manage, and build multi-phase jobs. we specialize in excavation, foundation, Roofing and waterproofing.</p>
    </section>

    <section class="info why">
      <h2>WHY <span class="accent">CHOOSE US?</span></h2>
      <p>We work with architects and designers to produce beautiful, functional structures. Call us today and bring our project management skills and extensive construction experience to your next project.</p>
    </section>

    <ul class="services">
      <li><svg viewBox="0 0 12 12"><circle cx="6" cy="6" r="5" fill="none" stroke="#c9a43a" stroke-width="1.2"/><path d="M3.5 6.2l1.8 1.7 3.3-3.6" fill="none" stroke="#c9a43a" stroke-width="1.3"/></svg>Concrete Flatwork</li>
      <li><svg viewBox="0 0 12 12"><circle cx="6" cy="6" r="5" fill="none" stroke="#c9a43a" stroke-width="1.2"/><path d="M3.5 6.2l1.8 1.7 3.3-3.6" fill="none" stroke="#c9a43a" stroke-width="1.3"/></svg>Concrete Repair</li>
      <li><svg viewBox="0 0 12 12"><circle cx="6" cy="6" r="5" fill="none" stroke="#c9a43a" stroke-width="1.2"/><path d="M3.5 6.2l1.8 1.7 3.3-3.6" fill="none" stroke="#c9a43a" stroke-width="1.3"/></svg>Concrete Sidewalks</li>
      <li><svg viewBox="0 0 12 12"><circle cx="6" cy="6" r="5" fill="none" stroke="#c9a43a" stroke-width="1.2"/><path d="M3.5 6.2l1.8 1.7 3.3-3.6" fill="none" stroke="#c9a43a" stroke-width="1.3"/></svg>Patios &amp; Driveways</li>
      <li><svg viewBox="0 0 12 12"><circle cx="6" cy="6" r="5" fill="none" stroke="#c9a43a" stroke-width="1.2"/><path d="M3.5 6.2l1.8 1.7 3.3-3.6" fill="none" stroke="#c9a43a" stroke-width="1.3"/></svg>Stoops, Porches And Staircase</li>
      <li><svg viewBox="0 0 12 12"><circle cx="6" cy="6" r="5" fill="none" stroke="#c9a43a" stroke-width="1.2"/><path d="M3.5 6.2l1.8 1.7 3.3-3.6" fill="none" stroke="#c9a43a" stroke-width="1.3"/></svg>Foundation Contractors--Concrete</li>
      <li><svg viewBox="0 0 12 12"><circle cx="6" cy="6" r="5" fill="none" stroke="#c9a43a" stroke-width="1.2"/><path d="M3.5 6.2l1.8 1.7 3.3-3.6" fill="none" stroke="#c9a43a" stroke-width="1.3"/></svg>Facade Restoration</li>
      <li><svg viewBox="0 0 12 12"><circle cx="6" cy="6" r="5" fill="none" stroke="#c9a43a" stroke-width="1.2"/><path d="M3.5 6.2l1.8 1.7 3.3-3.6" fill="none" stroke="#c9a43a" stroke-width="1.3"/></svg>Concrete</li>
      <li><svg viewBox="0 0 12 12"><circle cx="6" cy="6" r="5" fill="none" stroke="#c9a43a" stroke-width="1.2"/><path d="M3.5 6.2l1.8 1.7 3.3-3.6" fill="none" stroke="#c9a43a" stroke-width="1.3"/></svg>Patios</li>
      <li><svg viewBox="0 0 12 12"><circle cx="6" cy="6" r="5" fill="none" stroke="#c9a43a" stroke-width="1.2"/><path d="M3.5 6.2l1.8 1.7 3.3-3.6" fill="none" stroke="#c9a43a" stroke-width="1.3"/></svg>Driveways</li>
      <li><svg viewBox="0 0 12 12"><circle cx="6" cy="6" r="5" fill="none" stroke="#c9a43a" stroke-width="1.2"/><path d="M3.5 6.2l1.8 1.7 3.3-3.6" fill="none" stroke="#c9a43a" stroke-width="1.3"/></svg>Walkways</li>
      <li><svg viewBox="0 0 12 12"><circle cx="6" cy="6" r="5" fill="none" stroke="#c9a43a" stroke-width="1.2"/><path d="M3.5 6.2l1.8 1.7 3.3-3.6" fill="none" stroke="#c9a43a" stroke-width="1.3"/></svg>Commercial Concrete Work</li>
      <li><svg viewBox="0 0 12 12"><circle cx="6" cy="6" r="5" fill="none" stroke="#c9a43a" stroke-width="1.2"/><path d="M3.5 6.2l1.8 1.7 3.3-3.6" fill="none" stroke="#c9a43a" stroke-width="1.3"/></svg>Concrete Restoration</li>
      <li><svg viewBox="0 0 12 12"><circle cx="6" cy="6" r="5" fill="none" stroke="#c9a43a" stroke-width="1.2"/><path d="M3.5 6.2l1.8 1.7 3.3-3.6" fill="none" stroke="#c9a43a" stroke-width="1.3"/></svg>Building Alterations</li>
      <li><svg viewBox="0 0 12 12"><circle cx="6" cy="6" r="5" fill="none" stroke="#c9a43a" stroke-width="1.2"/><path d="M3.5 6.2l1.8 1.7 3.3-3.6" fill="none" stroke="#c9a43a" stroke-width="1.3"/></svg>Foundations - Concrete</li>
      <li><svg viewBox="0 0 12 12"><circle cx="6" cy="6" r="5" fill="none" stroke="#c9a43a" stroke-width="1.2"/><path d="M3.5 6.2l1.8 1.7 3.3-3.6" fill="none" stroke="#c9a43a" stroke-width="1.3"/></svg>Concrete Repairs</li>
    </ul>

    <div class="footer-rule"></div>
    <footer class="footer">
      <div class="line" style="top:14px"></div>
      <div class="web-line"></div>
      <div class="web"><span>www.rbwxpo.com</span></div>
      <div class="line" style="bottom:14px"></div>
    </footer>
  </main>
</body>
</html>
```